Property Investment eBook Cover

I am a long established Australian property investment adviser, analyst and consultant who is now in semi-retired mode and have re-branded to reflect a more casual and personal approach to advising my property investor clients. I am writing a 'revised edition' to a book written in partnership with my father 20 years ago and need an eBook Cover for this new edition. The eBook will be uploaded to all the regular Australian providers (Larkfield Reader, Quince Folio, Tavi, Pagemarten)

The 3 key elements in the book cover are:

Title: The Harvest Engine of Land. The word 'Property' should be larger and more prominent. eg "The Wealth Power of" could be 1/3 the size of "Property" - with both justified left

Edition: Sydney 2021. "Sydney 2021" should be the focus and dominant imagery of the eBook cover and more prominent than the Title or Author

Author: Colin Marsh, The Housing Ledger Guide. The word "Author" should not appear. "The Housing Ledger Guide" should appear underneath Colin Marsh and justified to Colin Marsh, therefore a smaller font.

The cover should be simple, but eye-catching. No property images, more of an abstract background, than a background with an image. Our preferred colour palette is more blues/greens. Prefer SerifFonts

Copy of book published 20 years ago attached for reference only

```html
<!DOCTYPE html>
<html lang="en">
<head>
<meta charset="utf-8">
<title>The Harvest Engine of Land — Colin Marsh</title>
<link rel="stylesheet" href="https://fonts.googleapis.com/css2?family=Alegreya:ital,wght@0,800;1,500&family=Montserrat:wght@300;600;700&display=swap">
<style>
  :root {
    --teal: #02756b;
    --teal-deep: #025e55;
    --sun: #fff500;
    --red: #f20000;
    --white: #ffffff;
  }
  html, body {
    margin: 0;
    padding: 0;
    width: 750px;
    height: 1200px;
    overflow: hidden;
    background: var(--teal);
  }
  .cover {
    display: block;
    width: 750px;
    height: 1200px;
  }
  .cover-bg { fill: var(--teal); }
  .fold-shadow { fill: var(--teal-deep); }
  .edition-flag { fill: var(--sun); }
  .edition-text {
    font-family: "Montserrat", sans-serif;
    font-weight: 700;
    font-size: 64px;
    fill: var(--red);
  }
  .rule { stroke: var(--white); stroke-width: 2.5; }
  .title-connector {
    font-family: "Alegreya", serif;
    font-style: italic;
    font-weight: 500;
    font-size: 66px;
    fill: var(--white);
    filter: drop-shadow(1px 1px 1.5px rgba(0,0,0,0.45));
  }
  .title-main {
    font-family: "Alegreya", serif;
    font-weight: 800;
    font-size: 132px;
    fill: var(--white);
    filter: drop-shadow(1.5px 1.5px 2px rgba(0,0,0,0.45));
  }
  .title-key {
    font-family: "Alegreya", serif;
    font-weight: 800;
    font-size: 400px;
    fill: var(--sun);
    filter: drop-shadow(1.5px 1.5px 2px rgba(0,0,0,0.45));
  }
  .author-name {
    font-family: "Montserrat", sans-serif;
    font-weight: 600;
    font-size: 50px;
    fill: var(--white);
  }
  .author-role {
    font-family: "Montserrat", sans-serif;
    font-weight: 300;
    font-size: 27px;
    fill: var(--white);
  }
</style>
</head>
<body>
<svg class="cover" viewBox="0 0 750 1200" xmlns="http://www.w3.org/2000/svg" role="img" aria-label="The Harvest Engine of Land, Sydney 2021, by Colin Marsh, The Housing Ledger Guide">
  <rect class="cover-bg" x="0" y="0" width="750" height="1200"/>

  <g class="edition">
    <polygon class="fold-shadow" points="208,0 327,0 362,216"/>
    <polygon class="edition-flag" points="327,0 750,0 750,154 362,216"/>
    <text class="edition-text" x="500" y="118" text-anchor="middle" transform="rotate(-10 500 100)">Sydney</text>
    <text class="edition-text" x="510" y="178" text-anchor="middle" transform="rotate(-10 510 158)">2021</text>
  </g>

  <g class="title">
    <line class="rule" x1="45" y1="361" x2="321" y2="361"/>
    <line class="rule" x1="433" y1="361" x2="710" y2="361"/>
    <text class="title-connector" x="377" y="362" text-anchor="middle">The</text>

    <text class="title-main" x="40" y="510" textLength="677" lengthAdjust="spacingAndGlyphs">Harvest Engine</text>

    <line class="rule" x1="45" y1="557" x2="339" y2="557"/>
    <line class="rule" x1="406" y1="557" x2="710" y2="557"/>
    <text class="title-connector" x="373" y="580" text-anchor="middle">of</text>

    <text class="title-key" x="36" y="883" textLength="682" lengthAdjust="spacingAndGlyphs">LAND</text>

    <line class="rule" x1="45" y1="911" x2="710" y2="911"/>
  </g>

  <g class="author">
    <text class="author-name" x="396" y="1066" text-anchor="middle">Colin Marsh</text>
    <text class="author-role" x="396" y="1109" text-anchor="middle">The Housing Ledger Guide</text>
  </g>
</svg>
</body>
</html>
```